Business Card Design

Electronic Security
Alarm Systems
CCTV
Electronic Access Control
Security System Integration

Industry/Entity Type

Business

Contact Information for Business Card

Declan Whitfield
PO Box 862
Carrowbrook Qld 4179
Phone 07 38265014
Mob 0428615937

```html
<!DOCTYPE html>
<html lang="en">
<head>
<meta charset="utf-8">
<title>Declan Whitfield – Business Card</title>
<link href="https://fonts.googleapis.com/css2?family=Arimo:wght@400;700&display=swap" rel="stylesheet">
<style>
  :root {
    --backdrop: #2e2e30;
    --band-blue: #7cc4dd;
    --stripe-blue: #1a8cc0;
    --panel-light: #f5f5f5;
    --panel-shade: #d8d8d8;
    --ink: #111111;
    --ink-soft: #2a2a2a;
    --paper: #ffffff;
  }
  * { margin: 0; padding: 0; box-sizing: border-box; }
  html, body {
    width: 1200px; height: 997px; overflow: hidden;
    background: var(--backdrop);
    font-family: "Arimo", Arial, sans-serif;
  }
  .card {
    position: absolute; left: 370px; top: 132px;
    width: 460px; height: 733px;
    border-radius: 34px; overflow: hidden;
    background: var(--band-blue);
    display: flex; flex-direction: column;
  }
  .stripe { height: 8px; background: var(--stripe-blue); flex: none; }
  .card__header {
    height: 95px; text-align: center; padding-top: 26px; flex: none;
  }
  .card__name { font-weight: 700; font-size: 27px; color: var(--ink); letter-spacing: 0.3px; }
  .card__role { font-weight: 700; font-size: 18px; color: var(--paper); margin-top: 4px; }
  .card__phones {
    height: 47px; flex: none;
    display: flex; justify-content: space-around; align-items: center;
    font-weight: 700; font-size: 21px; color: var(--ink);
  }
  .phone { display: flex; align-items: center; gap: 8px; }
  .phone svg { width: 18px; height: 18px; }
  .card__brand {
    height: 314px; flex: none;
    background: linear-gradient(180deg, var(--panel-light), var(--panel-shade));
    display: flex; flex-direction: column; align-items: center; justify-content: center; gap: 22px;
  }
  .brand__dot { width: 120px; height: 120px; border-radius: 50%; background: var(--stripe-blue); }
  .brand__name {
    font-weight: 400; font-size: 40px; line-height: 1.1; color: var(--ink-soft); text-align: center;
  }
  .card__intro {
    height: 52px; flex: none; padding: 14px 0 0 30px;
    font-weight: 700; font-size: 22px; color: var(--paper);
  }
  .card__services {
    flex: 1; padding: 22px 26px 0 30px;
    font-weight: 700; font-size: 25px; line-height: 1.5; color: var(--ink);
  }
</style>
</head>
<body>
  <article class="card">
    <header class="card__header">
      <h1 class="card__name">Declan Whitfield</h1>
      <p class="card__role">Owner</p>
    </header>
    <div class="stripe"></div>
    <div class="card__phones">
      <span class="phone">
        <svg viewBox="0 0 24 24" aria-hidden="true"><path fill="#111" d="M3 8c0-2 4-4 9-4s9 2 9 4v2h-5V8H8v2H3zM6 12h12l2 8H4z"/></svg>
        0738265014
      </span>
      <span class="phone">
        <svg viewBox="0 0 24 24" aria-hidden="true"><rect x="6" y="2" width="12" height="20" rx="2" fill="none" stroke="#111" stroke-width="2"/><rect x="9" y="18" width="6" height="1.5" fill="#111"/></svg>
        0428615937
      </span>
    </div>
    <div class="stripe"></div>
    <section class="card__brand">
      <div class="brand__dot"></div>
      <p class="brand__name">Halden<br>Secure Systems</p>
    </section>
    <div class="stripe"></div>
    <p class="card__intro">We deals in</p>
    <div class="stripe"></div>
    <p class="card__services">CCTV,Alarm Systems,Electronic Security ,Electronic Access Control,Security System Integration</p>
  </article>
</body>
</html>
```